Social Media Monitoring Web Site Design

We need a responsive web design for a new company based in Ireland. We offer a social media monitoring service that works in a call centre environment. Our service name is 'VANTO'. We have a logo that is attached.

Sites we like (in no particular order):

1. http://www.plumvector.com/
2. https://taldrix.io/
3. https://www.loomhaven.com/

We want the web site to have the following sections:

HOME
VANTO PLATFORM
VANTO SERVICE
CASE STUDIES
ABOUT US
CONTACT US

We also need a customer Login link. The site must be a responsive design.

Target Market(s)

Corporate Customers

Industry/Entity Type

It Company

Coding

Coded - Design and coding required

Number of Pages Required

2 page

Requirements
Must have
• Responsive Design
• Bootstrap
Nice to have
• Animations

```html
<!DOCTYPE html>
<html lang="en">
<head>
<meta charset="utf-8">
<title>VANTO — Social Media Monitoring</title>
<link rel="stylesheet" href="https://fonts.googleapis.com/css2?family=Montserrat:wght@400;600;700&family=Open+Sans:wght@400;600&display=swap">
<style>
:root{
  --blue:#1a9ad6;
  --orange:#f47b20;
  --dark:#2d2f31;
  --darker:#232425;
  --ink:#333638;
  --muted:#8a8d90;
  --white:#ffffff;
  --head:'Montserrat',sans-serif;
  --body:'Open Sans',sans-serif;
}
*{box-sizing:border-box;margin:0;padding:0}
html,body{width:1200px;height:3152px;overflow:hidden}
body{position:relative;font-family:var(--body);color:var(--ink);background:var(--white)}
.abs{position:absolute}
section,footer{position:absolute;left:0;width:1200px;overflow:hidden}

/* hero */
.hero{top:0;height:603px;background:linear-gradient(135deg,#3b3f44 0%,#24272b 45%,#34383c 100%)}
.hero-photo{position:absolute;inset:0;background:radial-gradient(ellipse at 70% 60%,rgba(120,130,140,.35),transparent 60%),radial-gradient(ellipse at 20% 40%,rgba(90,95,100,.3),transparent 55%)}
.brand{display:flex;align-items:center;gap:10px;font-family:var(--head);font-weight:700;font-size:30px;letter-spacing:3px;color:var(--white)}
.brand-mark{width:14px;height:14px;background:var(--orange)}
.nav{top:46px;left:504px;height:16px;width:440px;font-family:var(--head);font-size:12px;font-weight:600;color:var(--white)}
.nav a{color:inherit;text-decoration:none;position:absolute;top:0;white-space:nowrap}
.nav .active{color:var(--orange)}
.login{top:38px;left:950px;width:79px;height:32px;background:var(--blue);color:var(--white);font-family:var(--head);font-size:12px;font-weight:600;display:flex;align-items:center;justify-content:center;border-radius:2px}
.hero-title{top:170px;left:0;width:1200px;text-align:center;font-family:var(--head);font-size:45px;line-height:56px;color:var(--white);font-weight:400}
.hero-title .b{color:var(--blue)} .hero-title .o{color:var(--orange)}
.hero-text{top:302px;left:210px;width:780px;text-align:center;font-size:15px;line-height:26px;color:#d8d8d8}
.btn{display:flex;align-items:center;justify-content:center;font-family:var(--head);font-weight:700;font-size:13px;color:var(--white);text-transform:uppercase;letter-spacing:.3px;white-space:nowrap}
.btn-orange{background:var(--orange)}
.btn-blue{background:var(--blue)}
.btn-line{border:2px solid var(--white)}
.dots{top:548px;left:547px;display:flex;gap:4px}
.dots span{width:34px;height:3px;background:rgba(255,255,255,.55)}
.dots span:first-child{background:var(--white)}

/* headings */
.sec-title{left:0;width:1200px;text-align:center;font-family:var(--head);font-weight:700;font-size:22px;letter-spacing:.5px}
.rule{left:578px;display:flex;gap:6px}
.rule i{display:block;width:19px;height:4px;transform:skewX(-30deg)}
.rule i:first-child{background:var(--orange)} .rule i:last-child{background:var(--blue)}

/* welcome */
.welcome{top:603px;height:590px;background:var(--white)}
.welcome-text{top:140px;left:180px;width:844px;text-align:center;font-size:12px;line-height:22px;color:var(--muted)}
.feature{width:210px;text-align:center}
.feature-icon{width:100px;height:100px;margin:0 auto;border-radius:50%;background:var(--blue);border:5px solid #e4e4e4;box-shadow:0 0 0 2px #d0d0d0 inset;display:flex;align-items:center;justify-content:center}
.feature h3{margin-top:24px;font-family:var(--head);font-weight:600;font-size:15px;line-height:22px;color:var(--ink)}
.feature p{margin-top:16px;font-size:12px;line-height:22px;color:var(--muted)}

/* services */
.services{top:1193px;height:581px;background:linear-gradient(120deg,#6d7680 0%,#4a535d 40%,#5d666f 100%)}
.services-photo{position:absolute;inset:0;background:linear-gradient(rgba(30,40,50,.45),rgba(30,40,50,.55))}
.monitor-frame{left:119px;top:180px;width:538px;height:340px;background:#111;border-radius:12px 12px 0 0;padding:18px 18px 0}
.monitor-screen{width:100%;height:100%;background:linear-gradient(180deg,#f5f6f7 0 12%,#ffffff 12%),#fff}
.monitor-chin{left:119px;top:520px;width:538px;height:44px;background:linear-gradient(#d8dadc,#b8bbbe)}
.monitor-stand{left:335px;top:564px;width:106px;height:20px;background:#c4c6c8}
.checks{left:714px;top:180px;list-style:none;color:var(--white);font-family:var(--head);font-size:15px;font-weight:600}
.checks li{position:absolute;left:0;display:flex;align-items:center;gap:20px;white-space:nowrap}

/* case studies */
.cases{top:1774px;height:477px;background:var(--blue)}
.case{display:flex;gap:11px;color:var(--white)}
.case-photo{width:88px;height:144px;flex:none}
.case-num{font-family:var(--head);font-weight:700;font-size:44px;line-height:44px}
.case h3{margin-top:8px;font-family:var(--head);font-weight:600;font-size:15px}
.case p{margin-top:6px;font-size:12px;line-height:17px;width:320px}
.case .more{margin-top:8px;font-family:var(--head);font-weight:700;font-size:13px}

/* testimonials */
.testimonials{top:2251px;height:383px;background:linear-gradient(135deg,#f6f6f6,#e9e9e9 50%,#f4f4f4)}
.avatar{width:94px;height:94px;border-radius:50%;border:4px solid var(--white);box-shadow:0 1px 4px rgba(0,0,0,.15)}
.quote h3{font-family:var(--head);font-weight:600;font-size:16px;letter-spacing:.5px;color:var(--ink)}
.quote p{margin-top:12px;font-size:12px;line-height:19px;color:var(--muted);width:290px}
.quote .by{margin-top:14px;font-size:12px;color:var(--muted)}
.quote .by b{color:var(--orange);font-weight:600}

/* footer */
.footer{top:2634px;height:432px;background:var(--dark);color:var(--white)}
.social{display:flex;gap:13px}
.social span{width:34px;height:34px;border-radius:50%;background:var(--white)}
.col h4{font-family:var(--head);font-weight:700;font-size:14px;letter-spacing:.5px;white-space:nowrap}
.col ul{list-style:none;margin-top:26px;font-size:12px;color:#b8babc}
.col li{height:29px}
.email-field{left:763px;top:232px;width:169px;height:36px;background:#191a1b;display:flex;align-items:center;padding-left:14px;font-family:var(--head);font-size:11px;font-weight:600}
.signup{left:941px;top:232px;width:97px;height:36px}
.contact-line{left:763px;display:flex;align-items:center;gap:12px;font-size:12px;color:#b8babc}
.bottom{top:3066px;height:86px;background:var(--darker);color:#9a9c9e;font-size:12px}
</style>
</head>
<body>

<section class="hero">
  <div class="hero-photo" role="img" aria-label="Photo of a desk with a laptop and keyboard in dim light"></div>
  <div class="abs brand" style="left:175px;top:36px"><span class="brand-mark"></span>VANTO</div>
  <nav class="abs nav">
    <a class="active" style="left:0">Home</a>
    <a style="left:56px">Platform</a>
    <a style="left:129px">Services</a>
    <a style="left:198px">Case Studies</a>
    <a style="left:297px">About Us</a>
    <a style="left:371px">Contact</a>
  </nav>
  <div class="abs login">Login</div>
  <h1 class="abs hero-title">When it comes to <span class="b">safety</span>, we don't<br>believe in <span class="o">compromise</span></h1>
  <p class="abs hero-text">Lorem ipsum dolor sit amet, consectetur adipiscing elit. Aenean turpis urna, tincidunt sed tristique et, pulvinar eget risus. Ut euismod sagittis nibh, sed gravida nulla pellentesque eget.</p>
  <div class="abs btn btn-orange" style="left:387px;top:400px;width:203px;height:46px">Try it free now!</div>
  <div class="abs btn btn-line" style="left:608px;top:400px;width:205px;height:46px">Learn more about us</div>
  <div class="abs dots"><span></span><span></span><span></span><span></span></div>
</section>

<section class="welcome">
  <h2 class="abs sec-title" style="top:64px">WELCOME TO VANTO</h2>
  <div class="abs rule" style="top:100px"><i></i><i></i></div>
  <p class="abs welcome-text">Lorem ipsum dolor sit amet, consectetur adipiscing elit. Etiam mollis, neque eget iaculis faucibus, enim ipsum bibendum elit, congue commodo dolor mi at lacus. Ut egestas lectus at libero bibendum ultrices. Morbi venenatis, sem quis faucibus volutpat, mi turpis tincidunt mauris, quis placerat magna arcu ac sem. Cras laoreet turpis ac pulvinar vestibulum. Curabitur ac sapien sit amet massa viverra molestie. Donec consequat eu purus condimentum accumsan. Donec varius sed nulla vel ultricies. Quisque finibus cursus eros ac consectetur.</p>

  <div class="abs feature" style="left:165px;top:280px">
    <div class="feature-icon"><svg width="46" height="40" viewBox="0 0 46 40" fill="none" stroke="#fff" stroke-width="3" stroke-linejoin="round"><path d="M3 4h26v17H13l-6 6v-6H3z"/><path d="M33 12h10v16h-4v6l-6-6H19v-4"/></svg></div>
    <h3>enim ipsum bindum<br>eliter eter</h3>
    <p>Lorem ipsum dolor sit amet,<br>consectetur adipiscing elit.<br>Etiam mollis,</p>
  </div>
  <div class="abs feature" style="left:377px;top:280px">
    <div class="feature-icon"><svg width="42" height="42" viewBox="0 0 42 42" fill="none" stroke="#fff" stroke-width="3"><circle cx="21" cy="21" r="17"/><path d="M28 14l-4 10-10 4 4-10z" fill="#fff"/></svg></div>
    <h3>enim ipsum bindum<br>eliter eter</h3>
    <p>Lorem ipsum dolor sit amet,<br>consectetur adipiscing elit.<br>Etiam mollis,</p>
  </div>
  <div class="abs feature" style="left:593px;top:280px">
    <div class="feature-icon"><svg width="42" height="42" viewBox="0 0 42 42" fill="none" stroke="#fff" stroke-width="3"><circle cx="31" cy="9" r="5"/><circle cx="10" cy="21" r="5"/><circle cx="31" cy="33" r="5"/><path d="M15 18l12-7M15 24l12 7"/></svg></div>
    <h3>enim ipsum bindum<br>eliter eter</h3>
    <p>Lorem ipsum dolor sit amet,<br>consectetur adipiscing elit.<br>Etiam mollis,</p>
  </div>
  <div class="abs feature" style="left:807px;top:280px">
    <div class="feature-icon"><svg width="44" height="44" viewBox="0 0 44 44" fill="none" stroke="#fff" stroke-width="3"><path d="M10 22a12 12 0 0 1 24 0"/><rect x="6" y="20" width="6" height="10" rx="2" fill="#fff"/><rect x="32" y="20" width="6" height="10" rx="2" fill="#fff"/><circle cx="22" cy="22" r="6" fill="#fff"/><path d="M12 40c2-6 6-8 10-8s8 2 10 8" fill="#fff"/></svg></div>
    <h3>enim ipsum bindum<br>eliter eter</h3>
    <p>Lorem ipsum dolor sit amet,<br>consectetur adipiscing elit.<br>Etiam mollis,</p>
  </div>
</section>

<section class="services">
  <div class="services-photo" role="img" aria-label="Photo of a call centre team working at their desks"></div>
  <h2 class="abs sec-title" style="top:72px;color:var(--white)">VANTO SERVICES</h2>
  <div class="abs rule" style="top:108px"><i></i><i></i></div>
  <div class="abs monitor-frame"><div class="monitor-screen" role="img" aria-label="Screenshot of the monitoring dashboard"></div></div>
  <div class="abs monitor-chin"></div>
  <div class="abs monitor-stand"></div>
  <ul class="checks abs">
    <li style="top:0"><svg width="20" height="20" viewBox="0 0 20 20" fill="none" stroke="#f47b20" stroke-width="2"><path d="M17 9.5A7.5 7.5 0 1 1 12.5 3"/><path d="M6 9l4 4 8-9"/></svg>Integer eu dapibus felis.</li>
    <li style="top:45px"><svg width="20" height="20" viewBox="0 0 20 20" fill="none" stroke="#f47b20" stroke-width="2"><path d="M17 9.5A7.5 7.5 0 1 1 12.5 3"/><path d="M6 9l4 4 8-9"/></svg>Pellentesque lacinia velit at ante.</li>
    <li style="top:92px"><svg width="20" height="20" viewBox="0 0 20 20" fill="none" stroke="#f47b20" stroke-width="2"><path d="M17 9.5A7.5 7.5 0 1 1 12.5 3"/><path d="M6 9l4 4 8-9"/></svg>Id accumsan mauris vehicula</li>
    <li style="top:137px"><svg width="20" height="20" viewBox="0 0 20 20" fill="none" stroke="#f47b20" stroke-width="2"><path d="M17 9.5A7.5 7.5 0 1 1 12.5 3"/><path d="M6 9l4 4 8-9"/></svg>Praesent posuere rhoncus tempor</li>
    <li style="top:184px"><svg width="20" height="20" viewBox="0 0 20 20" fill="none" stroke="#f47b20" stroke-width="2"><path d="M17 9.5A7.5 7.5 0 1 1 12.5 3"/><path d="M6 9l4 4 8-9"/></svg>Nulla quis erat sit amet est.</li>
    <li style="top:229px"><svg width="20" height="20" viewBox="0 0 20 20" fill="none" stroke="#f47b20" stroke-width="2"><path d="M17 9.5A7.5 7.5 0 1 1 12.5 3"/><path d="M6 9l4 4 8-9"/></svg>Accumsan mauris vehicula id</li>
  </ul>
  <div class="abs btn btn-blue" style="left:714px;top:475px;width:137px;height:36px;font-size:12px">Learn more</div>
  <div class="abs btn btn-line" style="left:867px;top:475px;width:137px;height:36px;font-size:12px">Call us now</div>
</section>

<section class="cases">
  <div class="abs" style="inset:0;background:linear-gradient(180deg,rgba(255,255,255,.04),rgba(0,0,0,.04))" role="img" aria-label="Faint pattern of crowd portraits"></div>
  <h2 class="abs sec-title" style="top:76px;color:var(--white)">CASE STUDIES</h2>
  <div class="abs rule" style="top:112px"><i style="background:#fff"></i><i style="background:#fff"></i></div>
  <article class="abs case" style="left:171px;top:176px">
    <div class="case-photo" role="img" aria-label="Photo of a bright modern office" style="background:linear-gradient(160deg,#e9ecee,#9aa3aa)"></div>
    <div>
      <div class="case-num">01.</div>
      <h3>Major International Airline</h3>
      <p>Nulla vitae volutpat enim. Ut et ligula augue. Integer feugiat neque sapien, vulputate placerat magna.</p>
      <div class="more">READ MORE</div>
    </div>
  </article>
  <article class="abs case" style="left:619px;top:176px">
    <div class="case-photo" role="img" aria-label="Photo of a man in glasses" style="background:linear-gradient(160deg,#8a7a6c,#3f4a55)"></div>
    <div>
      <div class="case-num">02.</div>
      <h3>Major International Airline</h3>
      <p>Nulla vitae volutpat enim. Ut et ligula augue. Integer feugiat neque sapien, vulputate placerat magna.</p>
      <div class="more">READ MORE</div>
    </div>
  </article>
  <div class="abs btn btn-line" style="left:498px;top:365px;width:204px;height:36px;font-size:12px;border-width:1px">Get the more case study</div>
</section>

<section class="testimonials">
  <h2 class="abs sec-title" style="top:82px;color:var(--ink)">CLIENT TESTIMONIALS</h2>
  <div class="abs rule" style="top:118px"><i></i><i></i></div>
  <div class="abs avatar" role="img" aria-label="Portrait of Jonathan Reed" style="left:173px;top:186px;background:linear-gradient(#c9b8a8,#6d7a86)"></div>
  <div class="abs quote" style="left:281px;top:183px">
    <h3>JONATHAN REED</h3>
    <p>Lorem ipsum dolor sit amet, consectetur adipiscing elit. Sed risus erat, maximus nec turpis nec, maximus accumsan enim.</p>
    <div class="by">Founder of <b>Company Inc.</b></div>
  </div>
  <div class="abs avatar" role="img" aria-label="Portrait of Brittany Vale" style="left:628px;top:186px;background:linear-gradient(#e2c6a2,#8c6a4c)"></div>
  <div class="abs quote" style="left:736px;top:183px">
    <h3>BRITTANY VALE</h3>
    <p>Lorem ipsum dolor sit amet, consectetur adipiscing elit. Sed risus erat, maximus nec turpis nec, maximus accumsan enim.</p>
    <div class="by">Founder of <b>Company Inc.</b></div>
  </div>
</section>

<footer class="footer">
  <div class="abs brand" style="left:173px;top:80px"><span class="brand-mark"></span>VANTO</div>
  <div class="abs social" style="left:911px;top:89px" aria-label="Social links"><span aria-label="Social link one"></span><span aria-label="Social link two"></span><span aria-label="Social link three"></span></div>

  <div class="abs col" style="left:160px;top:187px"><h4>QUICK LINKS</h4><ul><li>Home</li><li>Platform</li><li>Case Studies</li><li>Contact</li><li>Testimonials</li></ul></div>
  <div class="abs col" style="left:344px;top:187px"><h4>OUR COMPANY</h4><ul><li>About Us</li><li>Contact Us</li><li>The Team</li><li>Press</li><li>Partnerships</li></ul></div>
  <div class="abs col" style="left:549px;top:187px"><h4>VANTO SERVICES</h4><ul><li>Consectetur</li><li>Elit Sed Risus</li><li>Erat Maximus</li><li>Turpis Ccumsan</li><li>Sed Risus Elit</li></ul></div>
  <div class="abs col" style="left:763px;top:187px"><h4>STAY CONNECTED</h4></div>
  <div class="abs email-field">EMAIL ID</div>
  <div class="abs btn btn-blue signup" style="font-size:12px">Sign up</div>
  <div class="abs contact-line" style="top:291px"><svg width="14" height="14" viewBox="0 0 14 14"><path fill="#fff" d="M3 1l2.5 3-1.5 1.5c.8 1.8 2.2 3.2 4 4L9.5 8 13 10.5 11.5 13C6 13 1 8 1 2.5z"/></svg>(021) 555 0148</div>
  <div class="abs contact-line" style="top:321px"><svg width="14" height="12" viewBox="0 0 14 12"><rect x="0" y="1" width="14" height="10" fill="#fff"/><path d="M0 1l7 5 7-5" stroke="#2d2f31" stroke-width="1.4" fill="none"/></svg>support@vanto-mail.com</div>
</footer>

<div class="abs bottom" style="left:0;width:1200px">
  <span class="abs" style="left:163px;top:40px">© 2015 Vanto. All Rights Reserved</span>
  <span class="abs" style="left:822px;top:40px">Terms of Use&nbsp;&nbsp;•&nbsp;&nbsp;Privacy Policy</span>
</div>

</body>
</html>
```